KT Appraisals BV business cards (a financial services company)

I am looking for a business card design that stands out in the financial advisory field of business & intellectual property valuation. The business card design should be conservative, yet different. Address details have changed since the attached business card. New address is:

Dorpelstraat 27
4817 KM Leiden
The Netherlands

Telephone number remains the same.

```html
<!DOCTYPE html>
<html lang="en">
<head>
<meta charset="utf-8">
<title>KT Appraisals BV – Business Cards</title>
<link href="https://fonts.googleapis.com/css2?family=PT+Sans:wght@400;700&display=swap" rel="stylesheet">
<style>
  :root {
    --backdrop: #e4e5e7;
    --card: #ffffff;
    --ink: #1b1b1b;
    --muted: #8a8a8a;
    --brand: #8f8f8f;
    --band: #232323;
    --band-edge: #9a9a9a;
  }
  * { box-sizing: border-box; margin: 0; padding: 0; }
  html, body { width: 1200px; height: 1000px; overflow: hidden; }
  body {
    background: var(--backdrop);
    font-family: "PT Sans", sans-serif;
    position: relative;
  }
  .card {
    position: absolute;
    left: 250px;
    width: 700px;
    height: 400px;
    background: var(--card);
    border-radius: 22px;
    overflow: hidden;
    box-shadow: 0 10px 30px rgba(0,0,0,.18);
  }
  .card--front { top: 50px; }
  .card--back { top: 540px; }

  .brand {
    display: flex;
    align-items: center;
    gap: 14px;
    color: var(--brand);
    font-weight: 400;
    letter-spacing: 2px;
    text-transform: uppercase;
    white-space: nowrap;
  }
  .brand__mark {
    width: 22px; height: 22px;
    background: var(--brand);
    flex: none;
  }
  .card--front .brand {
    position: absolute;
    left: 0; right: 0; top: 160px;
    justify-content: center;
    font-size: 40px;
  }
  .card--front .brand__mark { width: 30px; height: 30px; }
  .front__web {
    position: absolute;
    left: 0; right: 0; top: 345px;
    text-align: center;
    color: var(--muted);
    font-size: 17px;
    letter-spacing: 4px;
  }

  .card--back .brand {
    position: absolute;
    left: 40px; top: 150px;
    font-size: 26px;
  }
  .back__divider {
    position: absolute;
    left: 365px; top: 70px;
    width: 2px; height: 220px;
    background: var(--ink);
  }
  .contact {
    position: absolute;
    left: 395px; top: 72px;
    color: var(--muted);
    font-size: 17px;
    line-height: 1.3;
  }
  .contact__name {
    color: var(--ink);
    font-weight: 700;
    font-size: 22px;
  }
  .contact__role { margin-bottom: 6px; }
  .contact__address { margin-bottom: 8px; }
  .contact__list { list-style: none; }
  .contact__list li {
    display: flex; align-items: center; gap: 10px;
    margin-bottom: 4px;
  }
  .contact__list svg { width: 15px; height: 15px; flex: none; fill: var(--ink); }
  .back__band {
    position: absolute;
    left: 0; bottom: 0;
    width: 700px; height: 130px;
  }
</style>
</head>
<body>
  <section class="card card--front">
    <div class="brand"><span class="brand__mark"></span>KT Appraisals</div>
    <p class="front__web">www.ktappraisals.com</p>
  </section>

  <section class="card card--back">
    <div class="brand"><span class="brand__mark"></span>KT Appraisals</div>
    <div class="back__divider"></div>
    <div class="contact">
      <p class="contact__name">Marten Hoek, CFA, ASA, RV</p>
      <p class="contact__role">Managing Director</p>
      <p class="contact__address">Dorpelstraat 27<br>4817 KM Leiden The Netherlands</p>
      <ul class="contact__list">
        <li>
          <svg viewBox="0 0 24 24"><path d="M6.6 10.8a15.1 15.1 0 0 0 6.6 6.6l2.2-2.2c.3-.3.7-.4 1-.2 1.1.4 2.3.6 3.6.6.6 0 1 .4 1 1V20c0 .6-.4 1-1 1A17 17 0 0 1 3 4c0-.6.4-1 1-1h3.5c.6 0 1 .4 1 1 0 1.3.2 2.5.6 3.6.1.3 0 .7-.2 1z"/></svg>
          +31 (0)70 555 0142
        </li>
        <li>
          <svg viewBox="0 0 24 24"><path d="M2 5h20v14H2zm2 2v.5l8 5 8-5V7zm0 2.8V17h16V9.8l-8 5z"/></svg>
          mhoek@ktappraisals.com
        </li>
        <li>
          <svg viewBox="0 0 24 24"><path d="M12 2a10 10 0 1 0 0 20 10 10 0 0 0 0-20zm0 2a8 8 0 0 1 6.9 4H15l-2 2 1 2h3l1 3-3 3v2.3A8 8 0 0 1 5 7.5L8 11l2 1v3l2 2v2.9A8 8 0 0 1 12 4z"/></svg>
          www.ktappraisals.com
        </li>
      </ul>
    </div>
    <svg class="back__band" viewBox="0 0 700 130" preserveAspectRatio="none" aria-hidden="true">
      <path d="M0 20 Q 380 70 700 125 L700 130 L0 130 Z" fill="var(--band)"/>
      <path d="M20 16 Q 380 58 700 118" fill="none" stroke="var(--band-edge)" stroke-width="3"/>
    </svg>
  </section>
</body>
</html>
```